Dr Lenora aesthetics - Grace Distilled

I need a logo design for a new aesthetics business in London. I am specialised in Botox, Dermal Fillers & Skin Pigmentation treatment. The slogan is Grace Distilled. I would like some of the writing on the card to be embossed. I would like a very elegant design with the following detail:

1. White and gray scale background. For the font colour try gold OR silver shades.
2. The business involves working on the face mostly. Anything that can be done with letter 'M'? Or any other logo?
3. The front of the card should have Dr Lenora Aesthetics and the slogan 'Grace Distilled'. The back should have my full name (Dr Lenora Brackwell), qualifications (MBBS MSC BSC), my website (www.ashfernclinicalcare.example), telephone number & email.
4. The back should also say treatments offered: ANTI-WRINKLE INJECTIONS. DERMAL FILLERS, LIP ENHANCEMENT, HYPERHYDROSIS. SKIN PIGMENTATION

Thank you very much
Updates

Project Deadline Extended
Reason: Delays in market research response. I would be grateful for an extension please. Many thanks

Target Market(s)

Female and male aged 18 and above

Industry/Entity Type

Business

Contact Information for Business Card

Elegant design. Square corners. British standard size. Horizontal design. Should contain the slogan, contact details.

Font styles to use
Script

Colors
c9c9c9
fbed22
ffffff
f5f5f5
000000

Requirements
Must have
• All that's mentioned above
Nice to have
• A logo with the outline of a female face. Or anything that can be done with the letter M of Lenora.
Should not have
• No colours like green / purple / orange

```html
<!DOCTYPE html>
<html lang="en">
<head>
<meta charset="utf-8">
<title>Business Card – Dr Lenora Aesthetics</title>
<link rel="stylesheet" href="https://fonts.googleapis.com/css2?family=Barlow:wght@300;400&family=Nunito+Sans:ital,wght@0,300;0,400;0,600;1,300&display=swap">
<style>
  :root {
    --page: #ffffff;
    --card-grey: #6d6e71;
    --card-white: #ffffff;
    --card-border: #9a9a9a;
    --mark-light: rgba(255, 255, 255, 0.82);
    --mark-fade: rgba(255, 255, 255, 0.35);
    --ink-light: #ffffff;
    --ink-soft: #e2e2e2;
    --ink-dark: #58595b;
    --ink-mid: #6d6e71;
    --ink-muted: #8a8a8a;
    --heading: #2b2b2b;
  }
  * { margin: 0; padding: 0; box-sizing: border-box; }
  html, body {
    width: 1200px;
    height: 900px;
    overflow: hidden;
    background: var(--page);
    font-family: "Nunito Sans", sans-serif;
  }
  .board {
    position: relative;
    width: 1200px;
    height: 900px;
  }
  .section-title {
    position: absolute;
    left: 34px;
    top: 36px;
    display: flex;
    align-items: center;
    gap: 3px;
    font-family: "Barlow", sans-serif;
    font-size: 18px;
    font-weight: 400;
    letter-spacing: 2.4px;
    text-transform: uppercase;
    color: var(--heading);
  }
  .section-title svg { display: block; }

  .card {
    position: absolute;
    top: 121px;
    width: 443px;
    height: 247px;
    text-align: center;
    overflow: hidden;
  }
  .card-front {
    left: 130px;
    background: var(--card-grey);
    color: var(--ink-light);
  }
  .card-back {
    left: 611px;
    background: var(--card-white);
    border: 1px solid var(--card-border);
    color: var(--ink-dark);
  }

  .monogram-area {
    position: absolute;
    left: 0;
    right: 0;
    top: 28px;
    height: 118px;
    background: linear-gradient(100deg, var(--mark-fade) 0%, var(--mark-light) 30%, var(--mark-light) 68%, var(--mark-fade) 100%);
  }

  .brand-name {
    position: absolute;
    left: 0; right: 0;
    top: 165px;
    font-size: 17px;
    font-weight: 400;
    letter-spacing: 1.7px;
    text-transform: uppercase;
  }
  .brand-slogan {
    position: absolute;
    left: 0; right: 0;
    top: 191px;
    font-size: 13px;
    font-style: italic;
    font-weight: 300;
    letter-spacing: 0.6px;
    color: var(--ink-soft);
  }
  .brand-web {
    position: absolute;
    left: 0; right: 0;
    top: 213px;
    font-size: 14px;
    font-weight: 400;
    letter-spacing: 0.3px;
  }
  .brand-web strong { font-weight: 600; }

  .holder-name {
    position: absolute;
    left: 0; right: 0;
    top: 75px;
    font-size: 14px;
    font-weight: 400;
    letter-spacing: 1.6px;
    text-transform: uppercase;
    color: var(--ink-dark);
  }
  .holder-quals {
    position: absolute;
    left: 0; right: 0;
    top: 93px;
    font-size: 10px;
    letter-spacing: 0.8px;
    color: var(--ink-muted);
  }
  .holder-phone {
    position: absolute;
    left: 0; right: 0;
    top: 122px;
    font-size: 22px;
    font-weight: 400;
    letter-spacing: 1.2px;
    color: var(--ink-dark);
  }
  .treatments {
    position: absolute;
    left: 0; right: 0;
    top: 192px;
    font-size: 12px;
    line-height: 19px;
    letter-spacing: 0.3px;
    text-transform: uppercase;
    color: var(--ink-dark);
    list-style: none;
  }
  .treatments .sep {
    font-size: 9px;
    vertical-align: 1px;
    padding: 0 1px;
  }
</style>
</head>
<body>
<main class="board">
  <h1 class="section-title">
    <svg width="20" height="14" viewBox="0 0 20 14" aria-hidden="true">
      <path d="M1 7 H18 M12 1 L18 7 L12 13" fill="none" stroke="#2b2b2b" stroke-width="1.3"/>
    </svg>
    Business Card
  </h1>

  <section class="card card-front" aria-label="Card front">
    <div class="monogram-area" role="img" aria-label="Place for the brand's flowing script monogram sweeping across the card"></div>
    <p class="brand-name">Dr Lenora Aesthetics</p>
    <p class="brand-slogan">grace distilled</p>
    <p class="brand-web">www.<strong>ashfernclinicalcare</strong>.example</p>
  </section>

  <section class="card card-back" aria-label="Card back">
    <p class="holder-name">Dr Lenora Brackwell</p>
    <p class="holder-quals">MBBS MSC BSC</p>
    <p class="holder-phone">0000 00 00 00</p>
    <ul class="treatments">
      <li>Anti-wrinkle injections <span class="sep">•</span> Dermal fillers <span class="sep">•</span> Hyperhydrosis</li>
      <li>Lip enhancement <span class="sep">•</span> Skin pigmentation</li>
    </ul>
  </section>
</main>
</body>
</html>
```